Visitenkarte und Briefpapier für Rechtsanwaltskanzlei
Zielgruppe
Neugründung einer Rechtsanwaltskanzlei für Strafrecht mit einem Anwalt
Aufgabenstellung
Ich möchte gerne Briefpapier und Visitenkarten mit einem schlichten aber professionellen Charakter für meine neue Rechtsanwaltskanzlei erstellen lassen. Die Erscheinung soll modern, sachlich und klar sein. Es soll kein Logo verwendet werden, sondern nur der Namensschriftzug "Dr. Harald Obst", gerne in Großbuchstaben. Siehe dazu beispielhaft die Design-Charakter der angegeben Links.
Die Visitenkarte sollen als druckfähiges PDF und das Briefpapier zusätzlich als Word-Dokument geliefert werden.

```html
<!DOCTYPE html>
<html lang="de">
<head>
<meta charset="utf-8">
<title>Dr. Harald Obst – Briefpapier und Visitenkarte</title>
<link rel="stylesheet" href="https://fonts.googleapis.com/css2?family=Arimo&family=Source+Sans+3:wght@400&family=Crimson+Pro:wght@300;400&display=swap">
<style>
  :root {
    --bg: #f7f7f7;
    --paper: #ffffff;
    --brand: #2d5780;
    --ink: #1d1d1d;
    --body: #3f3f3f;
    --muted: #8a8a8a;
    --sign: #3a2d7a;
  }
  * { margin: 0; padding: 0; box-sizing: border-box; }
  html, body { width: 1200px; height: 1000px; overflow: hidden; background: var(--bg); }
  .canvas { position: relative; width: 1200px; height: 1000px; }

  .sheet, .card {
    position: absolute;
    background: var(--paper);
    box-shadow: 2px 2px 4px rgba(0,0,0,.28);
  }
  .sheet { left: 95px; top: 101px; width: 533px; height: 754px; }
  .card { left: 706px; top: 374px; width: 373px; height: 208px; }

  .bar { position: absolute; background: var(--brand); }

  .wordmark .name {
    font-family: "Arimo", Arial, sans-serif;
    color: var(--ink);
    font-size: 19px;
    line-height: 1;
    letter-spacing: .2px;
    white-space: nowrap;
  }
  .wordmark .field {
    font-family: "Source Sans 3", sans-serif;
    color: var(--brand);
    font-size: 8.6px;
    letter-spacing: 2.35px;
    margin-top: 4px;
    white-space: nowrap;
  }

  .sheet .wordmark { position: absolute; left: 321px; top: 32px; }

  .sender-line {
    position: absolute; left: 81px; top: 103px;
    font-family: "Source Sans 3", sans-serif;
    font-size: 5.2px; color: #555;
  }

  .contact {
    position: absolute; left: 403px; top: 117px;
    font-family: "Source Sans 3", sans-serif;
    color: var(--muted); font-size: 7px; line-height: 8.3px;
  }
  .contact .contact-name { color: var(--brand); font-size: 9.6px; margin-bottom: 5px; }
  .contact .addr { margin-bottom: 7px; }
  .contact .row { line-height: 11.3px; }
  .contact .label { display: inline-block; width: 27px; }

  .recipient, .salutation, .letter-body, .signatory {
    position: absolute;
    font-family: "Crimson Pro", Georgia, serif;
    color: var(--body);
    font-weight: 300;
  }
  .recipient { left: 68px; top: 200px; font-size: 10.6px; line-height: 12.8px; }
  .salutation { left: 68px; top: 263px; font-size: 10.6px; }
  .letter-body {
    left: 67px; top: 302px; width: 411px;
    font-size: 10.4px; line-height: 12.7px;
    text-align: justify; hyphens: auto;
  }
  .letter-body p + p { margin-top: 12.7px; }

  .fold-mark { position: absolute; left: 0; width: 21px; height: 1px; background: #555; }

  .signature {
    position: absolute; left: 52px; top: 550px; width: 148px; height: 50px;
  }
  .signatory { left: 94px; top: 591px; font-size: 10.6px; line-height: 12.8px; }

  .bank-details {
    position: absolute; left: 0; top: 711px; width: 533px;
    text-align: center;
    font-family: "Source Sans 3", sans-serif;
    font-size: 6.4px; line-height: 13px; color: var(--muted);
  }

  .card .wordmark { position: absolute; left: 0; top: 59px; width: 100%; text-align: center; }
  .card .wordmark .name, .card .wordmark .field { display: inline-block; text-align: left; }
  .card .wordmark .inner { display: inline-block; text-align: left; }
  .card-contact {
    position: absolute; left: 0; top: 152px; width: 100%;
    text-align: center;
    font-family: "Source Sans 3", sans-serif;
    font-size: 7px; line-height: 11.3px; color: var(--muted);
    word-spacing: 1px;
  }
  .card-contact .gap { display: inline-block; width: 5px; }
</style>
</head>
<body>
<div class="canvas">

  <section class="sheet letterhead">
    <div class="bar" style="left:316px; top:0; width:217px; height:10px;"></div>

    <header class="wordmark">
      <div class="name">DR. HARALD OBST</div>
      <div class="field">FACHANWALT FÜR STRAFRECHT</div>
    </header>

    <div class="sender-line">Dr. Harald Obst – Kastanienweg 14/16 – 10319 Berlin</div>

    <address class="contact" style="font-style:normal;">
      <div class="contact-name">Dr. Harald Obst</div>
      <div class="addr">Kastanienweg 14/16<br>10319 Berlin</div>
      <div class="row"><span class="label">Telefon:</span>030/418273560</div>
      <div class="row"><span class="label">Telefax:</span>030/418273562</div>
      <div class="row"><span class="label">Mobil:</span>0176/29417385</div>
      <div class="row"><span class="label">E-Mail:</span>post@obst-kanzlei.de</div>
    </address>

    <div class="recipient">Herr.<br>Konrad Albers<br>Web Master<br>City</div>

    <div class="fold-mark" style="top:263px;"></div>
    <div class="fold-mark" style="top:501px;"></div>

    <div class="salutation">Lorem ipsum dolor sit amet:</div>

    <div class="letter-body" lang="la">
      <p>Li Europan lingues es membres del sam familie. Lor separat existentie es un myth. Por scientie, musica, sport etc, litot Europa usa li sam vocabular. Li lingues differe solmen in li grammatica, li pronunciation e li plu commun vocabules. Omnicos directe al desirabilite de un nov lingua franca: On refusa continuar payar custosi traductores. At solmen va esser necessi far uniform grammatica, pronunciation e plu sommun paroles.</p>
      <p>Ma quande lingues coalesce, li grammatica del resultant lingue es plu simplic e regulari quam ti del coalescent lingues. Li nov lingua franca va esser plu simplic e regulari quam li existent Europan lingues. It va esser tam simplic quam Occidental in fact, it va esser Occidental. A un Angleso it va semblar un simplificat Angles, quam un skeptic Cambridge amico dit me que Occidental es. Li Europan lingues es membres del sam familie. Lor separat existentie es un myth.</p>
      <p>Por scientie, musica, sport etc, litot Europa usa li sam vocabular. Li lingues differe solmen in li grammatica, li pronunciation e li plu commun vocabules. Omnicos directe al desirabilite de un nov lingua franca: On refusa continuar payar custosi traductores. At solmen va esser necessi far uniform grammatica, pronunciation e plu sommun paroles. Ma quande lingues coalesce, li grammatica del resultant lingue es plu simplic e regulari quam ti del coalescent lingues. Li nov lingua franca va esser plu simplic e regulari quam li existent Europan lingues. It va esser tam simplic</p>
    </div>

    <div class="signature" role="img" aria-label="Handschriftliche Unterschrift" style="background:linear-gradient(90deg, rgba(58,45,122,0) 0%, rgba(58,45,122,.08) 50%, rgba(58,45,122,0) 100%);"></div>

    <div class="signatory">JONAS&nbsp; BREHM<br>Manager</div>

    <div class="bank-details">
      Privatkonto: IBAN: DE27 1209 4410 0033 5187 42&nbsp; BIC: KRSTDEB1XXX Konto: 33518742 BLZ : 120 944 10<br>
      Geschäftskonto: IBAN : DE81 1209 4410 0033 5190 17 BIC: KRSTDEB1XXX Konto: 33519017 BLZ : 120 944 10
    </div>

    <div class="bar" style="left:191px; top:744px; width:152px; height:10px;"></div>
  </section>

  <section class="card business-card">
    <div class="bar" style="left:278px; top:0; width:95px; height:6px;"></div>

    <header class="wordmark">
      <div class="inner">
        <div class="name">DR. HARALD OBST</div><br>
        <div class="field">FACHANWALT FÜR STRAFRECHT</div>
      </div>
    </header>

    <address class="card-contact" style="font-style:normal;">
      Kastanienweg 14/16<span class="gap"></span>10319 Berlin<br>
      Telefon: 030/418273560<span class="gap"></span>Telefax:&nbsp; 030/418273562<span class="gap"></span>Mobil: 0176/29417385<br>
      E-Mail:&nbsp; post@obst-kanzlei.de
    </address>

    <div class="bar" style="left:139px; top:202px; width:95px; height:6px;"></div>
  </section>

</div>
</body>
</html>
```